Ridgeway Patrol Website Design

Hello Designers. I am an agency and am helping a security company get a better look. I have a new logo and a car done up. We are looking for a fresh look using the blue and the gold. Open to a complimentary color.

Here is the old site
https://moravanguard.com/

Here is another design for photos and everything. We weren't sold on it because we wanted to make it simple like the first one.

https://ww2.moravanguard.com/

Attached is also the copy I would like to put on there.

I am looking for tough, competent and simple. Our customers are contruction companies, event planners etc. It has to be clean and easy.

One thing we can't provide yet is photos. We are anticipating photos of our team with arms folded beside the car, close up of the owner with a logo'd shirt on. Pictures of an Ridgeway Patrol job site etc. (which most of the time is construction. They also do Mall security. You can see if you want to use stock photos for now.

I wanted to get the look of the front page done first. Hoping for something really awesome. Have fun.

```html
<!DOCTYPE html>
<html lang="en">
<head>
<meta charset="utf-8">
<title>Ridgeway Patrol — Home</title>
<link href="https://fonts.googleapis.com/css2?family=Saira:ital,wght@0,400;0,500;0,600;0,700;1,400&display=swap" rel="stylesheet">
<style>
:root{
  --navy:#0f2744;
  --blue:#174a74;
  --gold:#9a7b2e;
  --grey:#eeeeee;
  --text:#333a44;
  --muted:#6b7178;
  --white:#ffffff;
}
*{box-sizing:border-box;margin:0;padding:0}
html,body{width:1200px;height:4155px;overflow:hidden;background:var(--white)}
body{font-family:"Saira",sans-serif;color:var(--text)}
.page{position:relative;width:1200px;height:4155px;overflow:hidden}
.section{position:absolute;left:0;width:1200px;overflow:hidden}
.abs{position:absolute}
svg.bg{position:absolute;left:0;top:0}

.eyebrow{font-size:10px;letter-spacing:1px;color:var(--gold);text-transform:uppercase;font-weight:600;display:flex;align-items:center;gap:10px;white-space:nowrap}
.eyebrow::before{content:"";width:50px;height:1px;background:var(--gold)}
.eyebrow.center{justify-content:center;left:0;width:1200px}
.eyebrow.center::after{content:"";width:50px;height:1px;background:var(--gold)}
.heading{font-size:27px;font-weight:500;letter-spacing:.5px;color:var(--navy);line-height:35px;white-space:nowrap}
.heading.light{color:var(--white)}
.heading.center{left:0;width:1200px;text-align:center}
.btn{display:flex;align-items:center;justify-content:center;font-size:10px;font-weight:600;height:24px;border:2px solid var(--white);box-shadow:0 0 0 1px var(--blue);color:var(--white);background:var(--blue);white-space:nowrap}
.btn.gold{background:var(--gold);box-shadow:0 0 0 1px var(--gold)}
.social{width:28px;height:28px;border-radius:50%;background:var(--navy);display:block}
.social.gold{background:var(--gold)}
.arrow{width:24px;height:24px}

/* header */
.header{top:0;height:111px;background:var(--white)}
.brand{font-weight:700;font-size:20px;line-height:1;color:var(--navy);letter-spacing:.5px}
.call{font-size:13px;color:var(--gold);font-weight:600;white-space:nowrap}
.call b{color:var(--navy);font-weight:600}
.socials{display:flex;gap:10px}
.nav-link{position:absolute;top:70px;font-size:11.5px;font-weight:500;color:var(--navy);white-space:nowrap}
.nav-link.active{color:var(--gold)}
.nav-link.active::after{content:"";position:absolute;left:-12px;right:-12px;bottom:-10px;height:2px;background:var(--gold)}

/* hero */
.hero{top:111px;height:537px}
.hero-title{left:202px;top:113px;font-size:34px;line-height:44px;color:var(--white);font-weight:500;letter-spacing:.5px}
.dots-v{left:990px;top:200px;display:flex;flex-direction:column;gap:5px}
.dots-v i{width:9px;height:9px;border-radius:50%;border:1px solid var(--white);display:block}

/* about */
.about{top:648px;height:524px}
.about p{font-size:11px;line-height:19px;color:var(--muted);width:360px}
.about p b{color:var(--text);font-weight:600}

/* services + testimonials */
.mid{top:1172px;height:1427px;background:var(--white)}
.card{top:145px;width:262px;height:305px}
.card-overlay{position:absolute;left:0;right:0;bottom:0;height:170px;background:linear-gradient(180deg,rgba(15,39,68,0),rgba(15,39,68,.85))}
.card-title{position:absolute;left:24px;bottom:20px;font-size:17px;color:var(--white);font-weight:500}
.card-body{position:absolute;left:24px;top:140px;width:215px;color:var(--white)}
.card-body h3{font-size:17px;font-weight:500;margin-bottom:12px}
.card-body p{font-size:10px;line-height:14px;margin-bottom:12px}
.frame{border:1px solid #b9a77a;background:var(--white);padding:12px}
.quote-box{background:var(--gold);color:var(--white);padding:30px 40px}
.quote-box .mark{font-size:44px;line-height:30px;font-weight:500}
.quote-box p{font-style:italic;font-size:13px;line-height:22px;margin-top:12px}
.quote-box .who{margin-top:20px;font-size:11px;letter-spacing:.5px;font-weight:600}
.dots-h{display:flex;gap:6px}
.dots-h i{width:9px;height:9px;border-radius:50%;border:1px solid var(--blue);display:block}
.dots-h i.on{background:var(--blue)}

/* team */
.team{top:2599px;height:523px;background:var(--white)}
.member{top:141px;width:220px;text-align:center}
.member .pic{width:206px;height:200px;margin:0 auto}
.member h4{margin-top:28px;font-size:13px;color:var(--navy);font-weight:600}
.member p{font-size:10.5px;color:var(--muted)}

/* quote form */
.quote{top:3100px;height:448px}
.field{height:30px;border:1px solid #8aa6c1;font-size:9px;color:#d6e2ee;padding:7px 10px}

/* hiring */
.hiring{top:3548px;height:317px;background:var(--gold);color:var(--white)}
.hiring p{font-size:13px;line-height:22px}

/* footer */
.footer{top:3865px;height:290px;background:var(--navy);color:var(--white)}
.footer h5{font-size:12px;font-weight:600}
.footer .line{font-size:10px;line-height:14px;display:flex;gap:8px;white-space:nowrap}
.footer .links{font-size:10px;line-height:18.5px}
.footer small{font-size:10px}
.footer small em{color:var(--gold);font-style:normal}
</style>
</head>
<body>
<div class="page">

  <header class="section header">
    <div class="abs" style="left:93px;top:36px;display:flex;align-items:center;gap:8px">
      <span style="width:12px;height:12px;background:var(--gold);display:block"></span>
      <span class="brand">RIDGEWAY PATROL</span>
    </div>
    <div class="abs call" style="left:800px;top:22px">Call Us: <b>506.555.0142</b></div>
    <div class="abs socials" style="left:1005px;top:16px">
      <span class="social"></span><span class="social gold"></span><span class="social"></span>
    </div>
    <span class="nav-link active" style="left:448px">Home</span>
    <span class="nav-link" style="left:518px">About Us</span>
    <span class="nav-link" style="left:594px">Services</span>
    <span class="nav-link" style="left:666px">Our Team</span>
    <span class="nav-link" style="left:743px">Reviews</span>
    <span class="nav-link" style="left:812px">Contact Us</span>
    <div class="abs btn" style="left:888px;top:65px;width:116px;height:26px">Get a Free Quote</div>
  </header>

  <section class="section hero">
    <svg class="bg" width="1200" height="537" viewBox="0 0 1200 537">
      <defs>
        <linearGradient id="heroFill" x1="0" y1="0" x2="1" y2="1">
          <stop offset="0" stop-color="#6f7a88"/>
          <stop offset=".55" stop-color="#3b4656"/>
          <stop offset="1" stop-color="#1e2733"/>
        </linearGradient>
      </defs>
      <polygon points="234,400 600,537 966,400" fill="#9a7b2e"/>
      <polygon role="img" aria-label="Photo of security guards in dark uniforms at an event" points="0,0 1200,0 1200,335 600,507 0,335" fill="url(#heroFill)"/>
    </svg>
    <h1 class="abs hero-title">Ridgeway Patrol is an<br>Security For New Brunswick<br>Businesses &amp; Events</h1>
    <div class="abs btn gold" style="left:202px;top:265px;width:124px;height:24px">Contact Us Today!</div>
    <div class="abs dots-v"><i></i><i style="background:var(--white)"></i><i></i><i></i></div>
  </section>

  <section class="section about">
    <div class="abs" role="img" aria-label="Photo of a security guard speaking into a radio" style="left:202px;top:70px;width:385px;height:385px;background:linear-gradient(160deg,#8a929c,#2c3440)"></div>
    <div class="abs eyebrow" style="left:645px;top:58px">About Us</div>
    <h2 class="abs heading" style="left:645px;top:100px">Ridgeway Patrol is<br>New Brunswick owned<br>and operated.</h2>
    <p class="abs" style="left:645px;top:217px">We are committed to make sure your tools, and hard earned assets don't get stolen. We are there to make sure your event runs smooth and unwanted situations are prevented and/or taken care of. <b>You need eyes and ears 24/7. ...We are there. We're ready, so give us a call.</b></p>
    <p class="abs" style="left:645px;top:326px">New Brunswick resident Marcus Thibodeau is passionate about security, and doesn't like it when his New Brunswick neighbour's things get stolen and events aren't under control. The approach is to put things in place so these things don't happen ...</p>
    <div class="abs btn" style="left:647px;top:445px;width:116px">Explore More</div>
  </section>

  <section class="section mid">
    <svg class="bg" width="1200" height="1427" viewBox="0 0 1200 1427">
      <rect x="0" y="400" width="1200" height="1000" fill="#eeeeee"/>
      <polygon points="234,510 600,654 966,510" fill="#9a7b2e"/>
      <polygon points="0,0 1200,0 1200,446 600,614 0,446" fill="#174a74"/>
      <polygon points="234,1356 600,1427 966,1356" fill="#9a7b2e"/>
      <polygon points="0,1327 600,1400 1200,1327 1200,1427 0,1427" fill="#ffffff"/>
    </svg>
    <div class="abs eyebrow" style="left:202px;top:58px">What We Do</div>
    <h2 class="abs heading light" style="left:202px;top:88px">Services We Provide</h2>

    <svg class="abs arrow" style="left:136px;top:285px" viewBox="0 0 24 24"><path d="M15 4 7 12l8 8" fill="none" stroke="#fff" stroke-width="2"/></svg>
    <svg class="abs arrow" style="left:1043px;top:285px" viewBox="0 0 24 24"><path d="m9 4 8 8-8 8" fill="none" stroke="#fff" stroke-width="2"/></svg>

    <div class="abs card" role="img" aria-label="Photo of event security staff in a crowd" style="left:202px;background:linear-gradient(160deg,#8e96a0,#2a3340)">
      <div class="card-overlay"></div><div class="card-title">Event Security</div>
    </div>
    <div class="abs card" role="img" aria-label="Photo of a guard patrolling a retail store" style="left:470px;background:linear-gradient(160deg,#9aa3a0,#3a4350)">
      <div class="card-overlay" style="height:305px;background:rgba(15,39,68,.55)"></div>
      <div class="card-body">
        <h3>Retail Security</h3>
        <p>We provide all of our clients with a risk assessment of their property to ensure we provide the best deployment ...</p>
        <div class="btn" style="width:80px;background:transparent;box-shadow:0 0 0 1px #fff;border-color:transparent;background:#fff;color:var(--navy)">Read More</div>
      </div>
    </div>
    <div class="abs card" role="img" aria-label="Photo of a VIP protection officer beside a car" style="left:738px;background:linear-gradient(160deg,#a3a9b0,#2a3038)">
      <div class="card-overlay"></div><div class="card-title">VIP Security</div>
    </div>
    <div class="abs btn" style="left:556px;top:488px;width:88px;background:var(--navy)">View All</div>

    <div class="abs eyebrow center" style="top:719px">Testimonials</div>
    <h2 class="abs heading center" style="top:752px">What Our Customers Say</h2>
    <div class="abs frame" style="left:202px;top:796px;width:385px;height:428px">
      <div role="img" aria-label="Photo of a client on her phone escorted by a bodyguard" style="width:100%;height:100%;background:linear-gradient(150deg,#9a8f86,#2d2f36)"></div>
    </div>
    <div class="abs quote-box" style="left:577px;top:877px;width:423px;height:268px">
      <div class="mark">“</div>
      <p>“There are many variations of passages of Lorem Ipsum available, but the majority have suffered alteration in some form, by injected humour, or randomised words which don't look even slightly.”</p>
      <div class="who">STANDARD CHUNK</div>
    </div>
    <div class="abs dots-h" style="left:608px;top:1167px"><i></i><i class="on"></i><i></i><i></i><i></i></div>
    <div class="abs btn" style="left:556px;top:1263px;width:88px">View All</div>
  </section>

  <section class="section team">
    <div class="abs eyebrow center" style="top:64px">Talented Guard</div>
    <h2 class="abs heading center" style="top:96px">Meet The Team</h2>
    <svg class="abs arrow" style="left:136px;top:234px" viewBox="0 0 24 24"><path d="M15 4 7 12l8 8" fill="none" stroke="#0f2744" stroke-width="2"/></svg>
    <svg class="abs arrow" style="left:1043px;top:234px" viewBox="0 0 24 24"><path d="m9 4 8 8-8 8" fill="none" stroke="#0f2744" stroke-width="2"/></svg>

    <div class="abs member" style="left:217px">
      <svg class="pic" viewBox="0 0 206 200" role="img" aria-label="Portrait of guard Aaron Pelletier"><polygon points="103,4 200,26 186,140 103,196 20,140 6,26" fill="#2f3946" stroke="#9aa1a8" stroke-width="3"/></svg>
      <h4>Aaron Pelletier</h4><p>Lorem Ipsum simply dummy Post</p>
    </div>
    <div class="abs member" style="left:490px">
      <svg class="pic" viewBox="0 0 206 200" role="img" aria-label="Portrait of guard J. Whitford"><polygon points="103,4 200,26 186,140 103,196 20,140 6,26" fill="#3a4350" stroke="#9aa1a8" stroke-width="3"/></svg>
      <h4>J. Whitford</h4><p>Lorem Ipsum simply dummy Post</p>
    </div>
    <div class="abs member" style="left:764px">
      <svg class="pic" viewBox="0 0 206 200" role="img" aria-label="Portrait of guard Colin Arsenault"><polygon points="103,4 200,26 186,140 103,196 20,140 6,26" fill="#5a616b" stroke="#9aa1a8" stroke-width="3"/></svg>
      <h4>Colin Arsenault</h4><p>Lorem Ipsum simply dummy Post</p>
    </div>
    <div class="abs btn gold" style="left:547px;top:436px;width:106px">View All Team</div>
  </section>

  <section class="section quote">
    <svg class="bg" width="1200" height="448" viewBox="0 0 1200 448">
      <polygon points="0,190 600,22 1200,190 1200,448 0,448" fill="#9a7b2e"/>
      <polygon points="0,206 600,60 1200,206 1200,448 0,448" fill="#174a74"/>
    </svg>
    <div class="abs eyebrow center" style="top:128px">Contact Us</div>
    <h2 class="abs heading light center" style="top:160px">Get a Free Quote</h2>
    <div class="abs field" style="left:294px;top:224px;width:194px">Your Name</div>
    <div class="abs field" style="left:504px;top:224px;width:194px">Email</div>
    <div class="abs field" style="left:714px;top:224px;width:194px">Phone</div>
    <div class="abs field" style="left:294px;top:264px;width:614px;height:77px">Message ...</div>
    <div class="abs btn" style="left:555px;top:359px;width:90px;background:#fff;color:var(--navy)">Submit</div>
  </section>

  <section class="section hiring">
    <div class="abs" role="img" aria-label="Photo of a security officer in sunglasses and suit" style="left:760px;top:0;width:440px;height:317px;background:linear-gradient(90deg,rgba(154,123,46,1),rgba(90,85,70,.9) 45%,#2a2d33)"></div>
    <div class="abs" style="left:202px;top:66px;font-size:9px;letter-spacing:1px;font-weight:600">CAREERS</div>
    <h2 class="abs heading light" style="left:202px;top:88px">Now Hiring!</h2>
    <p class="abs" style="left:202px;top:140px;width:620px">We're looking for 10 professional part-time and full-time security officers. We want hard-working, punctual individuals that want to be part of a supportive and enriching team.</p>
    <div class="abs btn" style="left:204px;top:236px;width:86px;background:#fff;color:var(--gold);box-shadow:0 0 0 1px #fff;border-color:var(--gold)">Read More</div>
  </section>

  <footer class="section footer">
    <div class="abs" style="left:202px;top:70px;display:flex;align-items:center;gap:8px">
      <span style="width:12px;height:12px;background:var(--gold);display:block"></span>
      <span class="brand" style="color:var(--white);font-size:17px">RIDGEWAY PATROL</span>
    </div>
    <h5 class="abs" style="left:438px;top:58px">Contact Us</h5>
    <div class="abs line" style="left:438px;top:92px">
      <svg width="10" height="12" viewBox="0 0 10 12"><path d="M5 11S1 6.5 1 4a4 4 0 0 1 8 0c0 2.5-4 7-4 7z" fill="none" stroke="#9a7b2e" stroke-width="1.3"/><circle cx="5" cy="4" r="1.3" fill="#9a7b2e"/></svg>
      <span>2240 Harbourview Rd. Suite 300<br>Moncton NB E1C 4K2</span>
    </div>
    <div class="abs line" style="left:438px;top:130px">
      <svg width="10" height="12" viewBox="0 0 10 12"><path d="M2 1h2l1 3-1.5 1a6 6 0 0 0 3 3L7.5 6.5l3 1V10a1 1 0 0 1-1 1C4.5 11 1 7.5 1 2a1 1 0 0 1 1-1z" fill="#9a7b2e"/></svg>
      <span>(506) 555-0142</span>
    </div>
    <div class="abs line" style="left:438px;top:154px">
      <svg width="10" height="12" viewBox="0 0 10 12"><rect x=".5" y="2.5" width="9" height="7" fill="none" stroke="#9a7b2e"/><path d="m.5 2.5 4.5 4 4.5-4" fill="none" stroke="#9a7b2e"/></svg>
      <span>info@ridgewaypatrol.com</span>
    </div>
    <h5 class="abs" style="left:705px;top:58px">Quick Links</h5>
    <div class="abs links" style="left:705px;top:86px">Home<br>About Us<br>Services<br>Our Team<br>Reviews<br>Contact Us</div>
    <h5 class="abs" style="left:851px;top:58px">Follow Us</h5>
    <div class="abs socials" style="left:851px;top:92px">
      <span class="social" style="background:#fff"></span><span class="social gold"></span><span class="social" style="background:#fff"></span>
    </div>
    <small class="abs" style="left:202px;top:224px">© 2022 <em>Ridgeway Patrol</em>. All Right Reserved</small>
  </footer>

</div>
</body>
</html>
```